looking for sleek business card to standout from the crowd!

We are a young biotechnology company looking to help you personalize your health through understanding your genetic make up. We need you help in making a clean but sleek business card design using our new logo. The goal? Any time we give our cards out, people say "nice card!" The feel we are going for is "modern-techy". We don't want to come across as an old, giant pharma company, but not trying to be a hipster either.

Target Market(s)

healthcare and biotechnology industry.

Industry/Entity Type

Biotechnology

Contact Information for Business Card

Info to include on the card will be NAME, TITLE, EMAIL, PHONE. The companies website (www.corvalinbio.com) should also be on the card some where. Would like the logo, when printed, to be raised.

Requirements
Must have
• The logo we have attached in the color it is in. Fonts for text should lean toward more professional/tech.
Nice to have
• Prefer white/light color background
Should not have
• cartoons, landscape backgrounds images.

```html
<!DOCTYPE html>
<html lang="en">
<head>
<meta charset="utf-8">
<title>Corvalin Business Card</title>
<link href="https://fonts.googleapis.com/css2?family=Exo+2:wght@400;600;700;800&display=swap" rel="stylesheet">
<style>
  :root {
    --stage: #222222;
    --card-white: #fbfbfc;
    --brand-blue: #1273ba;
    --brand-green: #8cc63f;
    --divider: #9bbfdc;
  }
  * { margin: 0; padding: 0; box-sizing: border-box; }
  html, body { width: 1200px; height: 900px; overflow: hidden; }
  body {
    background: var(--stage);
    font-family: "Exo 2", Arial, sans-serif;
    position: relative;
  }
  .card {
    position: absolute;
    top: 271px;
    width: 457px;
    height: 281px;
    border-radius: 14px;
    overflow: hidden;
    background: var(--card-white);
    box-shadow: 3px 4px 6px rgba(0,0,0,0.45);
  }
  .card--front { left: 137px; }
  .card--back { left: 626px; }

  .wordmark {
    position: absolute;
    left: 0; right: 0;
    text-align: center;
    font-weight: 800;
    letter-spacing: 2px;
    white-space: nowrap;
  }
  .card--front .wordmark {
    top: 30px;
    font-size: 46px;
    color: var(--brand-blue);
  }

  .identity {
    position: absolute;
    right: 244px;
    top: 171px;
    text-align: right;
  }
  .identity__name {
    color: var(--brand-green);
    font-weight: 700;
    font-size: 22px;
    line-height: 24px;
    letter-spacing: 0.3px;
  }
  .identity__title {
    color: var(--brand-blue);
    font-weight: 600;
    font-size: 13px;
    line-height: 14px;
    letter-spacing: 0.4px;
  }
  .divider {
    position: absolute;
    left: 221px;
    top: 162px;
    width: 1px;
    height: 58px;
    background: var(--divider);
  }
  .contact {
    position: absolute;
    left: 231px;
    top: 159px;
    list-style: none;
  }
  .contact__item {
    display: flex;
    align-items: center;
    gap: 7px;
    height: 21px;
    color: var(--brand-blue);
    font-size: 13.5px;
  }
  .contact__icon { width: 15px; height: 15px; flex: none; }

  .back__band {
    position: absolute;
    left: 0; top: 0;
    width: 100%; height: 219px;
    background: var(--brand-blue);
  }
  .card--back .wordmark {
    top: 106px;
    font-size: 50px;
    color: #ffffff;
  }
  .back__web {
    position: absolute;
    left: 0; right: 0; top: 241px;
    text-align: center;
    color: var(--brand-blue);
    font-size: 13.5px;
  }
</style>
</head>
<body>
  <section class="card card--front">
    <div class="wordmark">CORVALIN</div>

    <div class="identity">
      <div class="identity__name">DANA REYES</div>
      <div class="identity__title">PRESIDENT</div>
    </div>
    <div class="divider"></div>
    <ul class="contact">
      <li class="contact__item">
        <svg class="contact__icon" viewBox="0 0 16 16"><circle cx="8" cy="8" r="8" fill="#1273ba"/><path d="M4 7.2c0-1.2 1.8-2 4-2s4 .8 4 2v.6h-2v-.8H6v.8H4z M5.2 8.4h5.6l.8 2.6H4.4z" fill="#fff"/></svg>
        <span>403- 555-0147</span>
      </li>
      <li class="contact__item">
        <svg class="contact__icon" viewBox="0 0 16 16"><circle cx="8" cy="8" r="8" fill="#1273ba"/><rect x="4" y="5" width="8" height="6" fill="#fff"/><path d="M4 5l4 3.2L12 5" fill="none" stroke="#1273ba" stroke-width="1"/></svg>
        <span>info@corvalinbio.com</span>
      </li>
      <li class="contact__item">
        <svg class="contact__icon" viewBox="0 0 16 16"><circle cx="8" cy="8" r="8" fill="#1273ba"/><circle cx="8" cy="8" r="4" fill="none" stroke="#fff" stroke-width="1.3"/><path d="M6 6.5l2.5 1 1 2.5" fill="none" stroke="#fff" stroke-width="1.2"/></svg>
        <span>www.corvalinbio.com</span>
      </li>
    </ul>
  </section>

  <section class="card card--back">
    <div class="back__band"></div>
    <div class="wordmark">CORVALIN</div>
    <div class="back__web">www.corvalinbio.com</div>
  </section>
</body>
</html>
```